Yard sign

I want it to look similar to this one,

change name to DRAVEK and submit new ideas

Also would like to improvise a bit. let's not make exactly the same thing

would like to change to: Connecticut #1 Company

also change phone to 203-555-0147
and website to
dravekllc.com

this is yard sign. size is 24' Width and 32' Height

Target Market(s)

Roof

Industry/Entity Type

Roofing

Requirements
Must have
• similar colors or add something new

```html
<!DOCTYPE html>
<html lang="en">
<head>
<meta charset="utf-8">
<title>Dravek Roofing Yard Sign</title>
<link rel="stylesheet" href="https://fonts.googleapis.com/css2?family=Anton&family=Oswald:wght@500;700&family=Arvo:wght@700&display=swap">
<style>
  :root {
    --sign-red: #ed1c24;
    --url-red: #cf1f2e;
    --ink: #000000;
    --paper: #ffffff;
    --banner-yellow: #fdd33c;
    --dot-yellow: #fff200;
    --outline-gray: #4d4d4f;
    --photo-light: #f0f0f0;
    --photo-mid: #bdbdbd;
    --photo-dark: #8c8c8c;
  }
  html, body {
    margin: 0;
    padding: 0;
    overflow: hidden;
    background: var(--paper);
  }
  .yard-sign {
    display: block;
    width: 900px;
    height: 1200px;
  }
  .tagline { font-family: "Oswald", sans-serif; font-weight: 700; fill: var(--ink); }
  .service { font-family: "Anton", sans-serif; fill: var(--sign-red); }
  .brand-name {
    font-family: "Anton", sans-serif;
    fill: var(--paper);
    stroke: var(--outline-gray);
    stroke-width: 10px;
    paint-order: stroke;
    stroke-linejoin: round;
  }
  .phone { font-family: "Anton", sans-serif; fill: var(--paper); }
  .phone-dot { fill: var(--dot-yellow); }
  .website { font-family: "Arvo", serif; font-weight: 700; }
  .website-name { fill: var(--url-red); }
  .website-tld { fill: var(--ink); }
  .site-marker { fill: var(--sign-red); }
</style>
</head>
<body>
<svg class="yard-sign" viewBox="0 0 900 1200" xmlns="http://www.w3.org/2000/svg">
  <defs>
    <linearGradient id="roof-photo-tone" x1="0" y1="0" x2="1" y2="1">
      <stop offset="0" stop-color="var(--photo-light)"/>
      <stop offset="0.55" stop-color="var(--photo-mid)"/>
      <stop offset="1" stop-color="var(--photo-dark)"/>
    </linearGradient>
  </defs>

  <rect class="roof-photo" x="0" y="0" width="900" height="620" fill="url(#roof-photo-tone)" role="img" aria-label="Grayscale photo of a roofer installing shingles on a pitched roof"/>

  <rect class="tagline-band" x="0" y="62" width="900" height="78" fill="var(--banner-yellow)"/>
  <text class="tagline" x="450" y="126" font-size="66" text-anchor="middle" textLength="800" lengthAdjust="spacingAndGlyphs">CONNECTICUT #1 COMPANY</text>

  <text class="service" x="35" y="452" font-size="330" textLength="830" lengthAdjust="spacingAndGlyphs">ROOFING</text>

  <polygon class="brand-panel" points="0,600 450,492 900,600 900,1050 0,1050" fill="var(--ink)"/>
  <polyline class="roof-ridge" points="0,600 450,492 900,600" fill="none" stroke="var(--sign-red)" stroke-width="12" stroke-linejoin="miter"/>

  <text class="brand-name" x="40" y="880" font-size="300" textLength="820" lengthAdjust="spacingAndGlyphs">DRAVEK</text>

  <text class="phone" x="45" y="1022" font-size="128" textLength="810" lengthAdjust="spacingAndGlyphs">203<tspan class="phone-dot">.</tspan>555<tspan class="phone-dot">.</tspan>0147</text>

  <rect class="accent-stripe" x="0" y="1050" width="900" height="12" fill="var(--sign-red)"/>

  <circle class="site-marker" cx="134" cy="1130" r="22"/>
  <text class="website" x="176" y="1150" font-size="84" textLength="608" lengthAdjust="spacingAndGlyphs"><tspan class="website-name">dravekllc</tspan><tspan class="website-tld">.com</tspan></text>
</svg>
</body>
</html>
```